Nutrition Infographic for weight loss- key points and nutrition habits for after weight loss surgery

I need someone to put together some infographics based on some nutrition information I have put together. We are a company who do weight loss surgery for patients and I am trying to put together some resources for patients so they can look after their nutrition for the long term.

I have some info and ideas on how we can execute this on paper but I need some a creative genius with top notch design skills to help me put it together.

I am basically after two infographics- One with the nutrition information I have outlined and One with the pyramid I have illustrated. Please let me know if you need clarification on the layout. Also happy to take on board any ideas you might have too!

If more time is needed with adjustments/refinements I understand and am happy to work with you to get to a final product we are happy with.

Target Market(s)

weight loss clients- ages ranging mostly from 20-45 male and female.

Industry/Entity Type

Health Care

Colors

Designer to choose colors to be used in the design.

Requirements
Must have
• Simple, clean concepts and images are needed.
• Easy to understand layout to enhance uptake of understanding the information

```html
<!DOCTYPE html>
<html lang="en">
<head>
<meta charset="utf-8">
<title>Good Nutrition Habits for Life</title>
<link rel="stylesheet" href="https://fonts.googleapis.com/css2?family=Montserrat:wght@600;700;800&family=Open+Sans:wght@400;600;700&display=swap">
<style>
  :root {
    --sky: #86d3e6;
    --sky-deep: #5fbfd8;
    --leaf: #8cc63f;
    --leaf-dark: #6aa52a;
    --panel: #ffffff;
    --ink: #ffffff;
    --ink-dark: #2b3a44;
    --accent: #f39a1e;
  }
  * { box-sizing: border-box; margin: 0; padding: 0; }
  html, body { width: 851px; height: 1200px; overflow: hidden; }
  body {
    background: var(--sky);
    font-family: "Open Sans", Arial, sans-serif;
    color: var(--ink);
  }
  .poster { width: 851px; height: 1200px; position: relative; }
  .masthead {
    height: 56px;
    background: var(--leaf);
    display: flex; align-items: center; justify-content: center;
    border-bottom: 4px solid var(--leaf-dark);
  }
  .masthead h1 {
    font-family: "Montserrat", Arial, sans-serif;
    font-weight: 800; font-size: 34px; color: #fff;
    letter-spacing: 0.3px;
    text-shadow: 0 2px 0 var(--accent);
  }
  .intro, .lead {
    margin: 0 34px;
    font-size: 13.6px; line-height: 1.38; font-weight: 600;
  }
  .intro { padding-top: 14px; }
  .intro p { margin-bottom: 9px; }
  .lead { margin-top: 10px; margin-bottom: 12px; }
  .lead strong { font-family: "Montserrat", Arial, sans-serif; font-weight: 800; }
  .row { display: flex; gap: 12px; margin: 0 28px 12px; height: 92px; }
  .group { display: flex; gap: 10px; height: 100%; }
  .group.wide { flex: 1; }
  .label {
    width: 178px; flex: none;
    background: var(--leaf);
    border-radius: 14px;
    display: flex; align-items: center; justify-content: center;
    text-align: center;
    font-family: "Montserrat", Arial, sans-serif;
    font-weight: 800; font-size: 15px; line-height: 1.2;
    padding: 6px 10px; color: #fff;
    box-shadow: 0 3px 0 var(--leaf-dark);
  }
  .label.narrow { width: 130px; }
  .items {
    flex: 1;
    background: var(--panel);
    border-radius: 14px;
    display: flex; align-items: center; justify-content: space-around;
    padding: 6px 8px;
  }
  .item { display: flex; flex-direction: column; align-items: center; gap: 4px; }
  .item .thumb { width: 62px; height: 54px; border-radius: 10px; }
  .item .thumb.big { width: 84px; }
  .item span { font-size: 11px; font-weight: 600; color: var(--ink-dark); }
  .t-red { background: linear-gradient(#f2b8a0, #d9684a); }
  .t-brown { background: linear-gradient(#d9b48a, #9c6a3c); }
  .t-cream { background: linear-gradient(#fbf4e2, #e9d8a8); }
  .t-blue { background: linear-gradient(#d6eef7, #8cc8e0); }
  .t-green { background: linear-gradient(#c8e49a, #6aa52a); }
  .t-mixed { background: linear-gradient(135deg, #f26b4a, #f6b93b 50%, #7cbf3f); }
  .t-pink { background: linear-gradient(#f9d3de, #e07ea0); }
  .t-dark { background: linear-gradient(#8a5a3c, #4b2e1e); }
  .t-gold { background: linear-gradient(#f8dc8a, #e0a23a); }
</style>
</head>
<body>
<main class="poster">
  <header class="masthead"><h1>Good Nutrition Habits for Life</h1></header>

  <section class="intro">
    <p>You have taken steps to lose weight and look after your health so we can take this opportunity to create some good nutrition habits for now and for the long term.</p>
    <p>You will learn to focus on food for nourishing your body with the right balance to keep you satisfied and to fuel yourself for journey ahead.</p>
    <p>To make things easier we are going to breakdown different food groups and prioritise them based on how much your body needs them.</p>
  </section>

  <p class="lead"><strong>EVERYDAY FOODS:</strong> Include these on a regular basis as they are generally whole foods, less processed and high in nutrient quality. There is no substitute for the naturally occurring vitamins, minerals and anti-oxidants which we find in food.</p>

  <div class="row">
    <div class="group wide">
      <div class="label">HIGH QUALITY PROTEINS</div>
      <div class="items">
        <div class="item"><div class="thumb t-brown" role="img" aria-label="Roast chicken"></div><span>Chicken</span></div>
        <div class="item"><div class="thumb t-red" role="img" aria-label="Cut of red meat"></div><span>Meat</span></div>
        <div class="item"><div class="thumb t-red" role="img" aria-label="Minced meat"></div><span>Mince</span></div>
        <div class="item"><div class="thumb t-pink" role="img" aria-label="Fish fillet"></div><span>Fish</span></div>
        <div class="item"><div class="thumb t-red" role="img" aria-label="Prawns"></div><span>Seafood</span></div>
        <div class="item"><div class="thumb t-cream" role="img" aria-label="Eggs"></div><span>Eggs</span></div>
      </div>
    </div>
  </div>

  <div class="row">
    <div class="group" style="width:380px">
      <div class="label narrow">DAIRY</div>
      <div class="items">
        <div class="item"><div class="thumb t-blue" role="img" aria-label="Glass of milk"></div><span>Milk</span></div>
        <div class="item"><div class="thumb t-gold" role="img" aria-label="Cheese"></div><span>Cheese</span></div>
        <div class="item"><div class="thumb t-cream" role="img" aria-label="Yoghurt tub"></div><span>Yoghurt</span></div>
      </div>
    </div>
    <div class="group wide">
      <div class="label narrow">FRESH FRUIT AND VEGETABLES</div>
      <div class="items">
        <div class="item"><div class="thumb big t-mixed" role="img" aria-label="Assorted fresh fruits"></div><span>Fresh Fruits</span></div>
        <div class="item"><div class="thumb big t-green" role="img" aria-label="Assorted vegetables"></div><span>Vegetables</span></div>
      </div>
    </div>
  </div>

  <div class="row">
    <div class="group wide">
      <div class="label">WHOLEGRAINS, QUALITY CARBS</div>
      <div class="items">
        <div class="item"><div class="thumb t-brown" role="img" aria-label="Multigrain bread"></div><span>Multigrain Bread</span></div>
        <div class="item"><div class="thumb t-cream" role="img" aria-label="Brown rice"></div><span>Brown rice</span></div>
        <div class="item"><div class="thumb t-cream" role="img" aria-label="Rolled oats"></div><span>Rolled oats</span></div>
        <div class="item"><div class="thumb t-red" role="img" aria-label="Sweet potato"></div><span>Sweet potato</span></div>
        <div class="item"><div class="thumb t-gold" role="img" aria-label="Quinoa"></div><span>Quinoa</span></div>
      </div>
    </div>
  </div>

  <div class="row">
    <div class="group wide">
      <div class="label">LEGUMES, PULSES, NUTS, SEEDS</div>
      <div class="items">
        <div class="item"><div class="thumb t-brown" role="img" aria-label="Mixed nuts"></div></div>
        <div class="item"><div class="thumb t-gold" role="img" aria-label="Lentils and pulses"></div></div>
        <div class="item"><div class="thumb t-cream" role="img" aria-label="Seeds"></div></div>
      </div>
    </div>
    <div class="group" style="width:340px">
      <div class="label narrow">HYDRATION</div>
      <div class="items">
        <div class="item"><div class="thumb t-blue" role="img" aria-label="Glass of water"></div><span>Water</span></div>
        <div class="item"><div class="thumb t-gold" role="img" aria-label="Cup of tea"></div><span>Tea</span></div>
        <div class="item"><div class="thumb t-dark" role="img" aria-label="Cup of coffee"></div><span>Coffee</span></div>
      </div>
    </div>
  </div>

  <p class="lead"><strong>SOMETIMES FOODS:</strong> These might have been a big part of your diet before you decided to take steps to improve your health and lose weight. Long term success does require some sacrifices and consistency so we will not include these items often.</p>

  <div class="row">
    <div class="group wide">
      <div class="label">SWEETS</div>
      <div class="items">
        <div class="item"><div class="thumb t-dark" role="img" aria-label="Chocolates"></div><span>Chocolates</span></div>
        <div class="item"><div class="thumb t-mixed" role="img" aria-label="Lollies"></div><span>Lollies</span></div>
        <div class="item"><div class="thumb t-pink" role="img" aria-label="Ice cream"></div><span>Ice Cream</span></div>
        <div class="item"><div class="thumb t-mixed" role="img" aria-label="Ice blocks"></div><span>Ice Blocks</span></div>
        <div class="item"><div class="thumb t-brown" role="img" aria-label="Biscuits"></div><span>Biscuits</span></div>
        <div class="item"><div class="thumb t-pink" role="img" aria-label="Cake slice"></div><span>Cakes</span></div>
      </div>
    </div>
  </div>

  <div class="row">
    <div class="group wide">
      <div class="label">HIGH SUGAR DRINKS</div>
      <div class="items">
        <div class="item"><div class="thumb t-red" role="img" aria-label="Soft drink cans"></div><span>Soft drinks</span></div>
        <div class="item"><div class="thumb t-gold" role="img" aria-label="Fruit juice"></div><span>Fruit juice</span></div>
        <div class="item"><div class="thumb t-gold" role="img" aria-label="Sweet iced tea"></div><span>Sweet iced teas</span></div>
        <div class="item"><div class="thumb t-green" role="img" aria-label="Energy drinks"></div><span>Energy drinks</span></div>
        <div class="item"><div class="thumb t-blue" role="img" aria-label="Sports drinks"></div><span>Sports drinks</span></div>
      </div>
    </div>
  </div>

  <div class="row">
    <div class="group wide">
      <div class="label">HIGH FAT CONTENT, POOR QUALITY FOODS</div>
      <div class="items">
        <div class="item"><div class="thumb t-gold" role="img" aria-label="Pastries"></div><span>Pastries</span></div>
        <div class="item"><div class="thumb t-brown" role="img" aria-label="Burger and fries"></div><span>Fast Food</span></div>
        <div class="item"><div class="thumb t-gold" role="img" aria-label="Potato crisps"></div><span>Crisps</span></div>
        <div class="item"><div class="thumb t-brown" role="img" aria-label="Fried foods"></div><span>Fried Foods</span></div>
      </div>
    </div>
  </div>
</main>
</body>
</html>
```